Not your average candle company needs label design

MOSS + RUIN A Brand Deck for Disruptive Candles
WHO WE ARE
Moss + Ruin is a disruptive candle brand built on contrast. We create clean-burning, scent-forward rituals for people who are both grounded and undone.
We’re not here for the beige wellness aesthetic. We’re here for the moments that are messy, bold, emotional, and beautifully real.
Rooted in botanical craftsmanship. Branded in poetic defiance.
WHAT WE WANT PEOPLE TO THINK
When someone encounters Moss + Ruin, we want them to feel like they’ve stumbled into something intimate, moody, and unforgettable.
We want them to think:
• “This brand gets me.”
• “This feels like design, emotion, and scent in one.”
• “It’s art I can burn.”
• “I’ve never seen a candle brand like this before.”
Our name alone sparks curiosity. Our story keeps them. Our product delivers.

Target Market(s)

Women and men ages 25–45 who appreciate thoughtful design and emotional storytelling People who love brands like Velmoria, Kid Scents, Heron Grange, Miravo, and La Fiole Design-minded buyers who shop indie, high-end, or artisanal and care about self-expression through scent Emotionally intelligent rebels. Introspective, edgy, but craving grounding rituals.

Industry/Entity Type

Candle Industry

Font styles to use
Other font styles liked:
• Moss should be more refined in a serif font and I like mistrully font for ruin.

Requirements
Must have
• Space for scent name and optionally, a small poetic tagline (like soft chaos. slow burn.) Layout that’s elegant but with tension — surprise us with something that doesn't play it safe Optional: room for batch no., burn time, scent notes on side or bottom. MOSS + RUIN soft chaos. slow burn. Scent name example: Troth Warden A silent vow to stay grounded. Earthy and grounding — like old books, soft shadows, and the quiet certainty of knowing who you are. [optional: 7 oz / 198g | coconut soy wax | 45+ hr burn time]
Nice to have
• raw edge opening with gold font. Open to colored labels. We’re creating an unforgettable candle brand called Moss + Ruin — a contrast-rich, emotionally resonant collection of candles that blend botanical beauty with bold edge. The name is intentional: Moss reflects grounding, ritual, and plant-based purity; Ruin speaks to vulnerability, chaos, and strength through contrast. Our brand is not dark or gothic — it’s confident, elevated, and style-forward, with packaging that feels like a cross between modern apothecary and high fashion. Think Miravo meets Dane Pellor. Gloss vessels, textured labels, contrasting fonts, and emotional scent storytelling.
Should not have
• goth vibe, typical candle label template layout.

```html
<!DOCTYPE html>
<html lang="en">
<head>
<meta charset="utf-8">
<title>Moss + Ruin — Troth Warden label</title>
<link href="https://fonts.googleapis.com/css2?family=Playfair+Display:wght@700&display=swap" rel="stylesheet">
<style>
  :root {
    --label-taupe: #c5bcaa;
    --label-taupe-deep: #b3a994;
    --ink-black: #141414;
    --steel-grey: #5a5955;
    --gold: #c9a15a;
    --text-white: #fbf9f4;
  }
  * { margin: 0; padding: 0; box-sizing: border-box; }
  html, body { width: 1200px; height: 1200px; overflow: hidden; }
  body {
    background: linear-gradient(160deg, var(--label-taupe) 0%, var(--label-taupe-deep) 100%);
    font-family: "Playfair Display", Georgia, serif;
    position: relative;
  }
  .label { position: absolute; inset: 0; }
  .helmet-art {
    position: absolute;
    left: 300px; top: 200px;
    width: 640px; height: 900px;
    border-radius: 46% 50% 40% 44% / 38% 40% 56% 52%;
    background:
      radial-gradient(ellipse 60% 40% at 55% 28%, var(--ink-black) 0%, #262524 60%, transparent 100%),
      radial-gradient(ellipse 55% 45% at 45% 72%, #3c3b38 0%, var(--steel-grey) 45%, #2a2928 80%, transparent 100%);
    filter: blur(6px);
    box-shadow: 0 0 60px 30px rgba(20,20,20,0.35);
  }
  .brand-name {
    position: absolute;
    left: 0; right: 0; top: 430px;
    padding-left: 40px;
    text-align: center;
    color: var(--gold);
    font-weight: 700;
    font-size: 104px;
    line-height: 1;
    letter-spacing: 2px;
    white-space: nowrap;
  }
  .scent {
    position: absolute;
    left: 0; right: 0; top: 735px;
    text-align: center;
    color: var(--text-white);
    font-weight: 700;
    padding-left: 40px;
  }
  .scent-name { font-size: 50px; letter-spacing: 1px; }
  .scent-tagline { font-size: 27px; margin-top: 14px; }
  .scent-weight { font-size: 23px; margin-top: 44px; }
</style>
</head>
<body>
  <main class="label">
    <div class="helmet-art" role="img" aria-label="Illustration of a plumed knight's helmet in profile, dark steel tones"></div>
    <p class="brand-name">MOSS + RUIN</p>
    <div class="scent">
      <p class="scent-name">TROTH WARDEN</p>
      <p class="scent-tagline">A silent vow to stay grounded</p>
      <p class="scent-weight">7.5oz-212g</p>
    </div>
  </main>
</body>
</html>
```